Basic Web Redesign

Hello,

We are working with a client who would like their existing website updated.

The site is http://www.lorenvasquel.com/

Currently the website is Joomla 1.0.x with Virtuemart running the small online shop.

We are extremely flexible with regards to the way forward - i.e. it can be Joomla 2.5 with Virtuemart, Wordpress plus a shopping cart, HTML 5 (no CMS) with a shopping cart or a full blown ecommerce solution using Prestashop, Magento etc.

The main constraint is a website that incorporates a working shop. At this moment the current website works, but is on extremely old versions of Joomla and Virtuemart.

So the brief is to either migrate the existing offering to a newer version of Joomla and Virtuemart OR use alternative products to achieve a very basic website with shopping cart functionality.

Reason: To enable designer to upload files and installation to be tested.

Target Market(s)

Predominantly people living on the Costa Blanca in Spain, but also some customers in the UK.

Industry/Entity Type

Shop

Requirements
Must have
• Online shop
Shipping calculator
Purselane for accepting payments
Nice to have
• Easy to use front-end for editing shop items
Easy to use front-end for editing non-shop pages

```html
<!DOCTYPE html>
<html lang="en">
<head>
<meta charset="utf-8">
<title>Loren Vasquel Floral Designer</title>
<link href="https://fonts.googleapis.com/css2?family=PT+Sans:ital,wght@0,400;0,700;1,400;1,700&family=Courgette&family=Marcellus&display=swap" rel="stylesheet">
<style>
:root{
  --magenta:#c8085f;
  --magenta-text:#d0126a;
  --green:#5f9a58;
  --green-dark:#4f8a4b;
  --green-title:#4f8a3a;
  --coral:#f45b4c;
  --lime:#a8cc3c;
  --peach:#f7a57c;
  --peach-light:#fbc09c;
  --grey-text:#4a4a4a;
  --footer-bg:#eeeeee;
  --white:#ffffff;
  --yellow:#ffd23c;
}
*{box-sizing:border-box;margin:0;padding:0}
html,body{width:960px;height:1200px;overflow:hidden}
body{position:relative;font-family:"PT Sans",sans-serif;color:var(--grey-text);background:#fdf7f7}
.blossom{position:absolute;top:0;width:140px;height:640px}
.blossom-left{left:0;background:radial-gradient(ellipse at 20% 30%,#f7c9cc 0%,#fbe3e3 45%,rgba(253,247,247,0) 75%)}
.blossom-right{right:0;background:radial-gradient(ellipse at 80% 50%,#f7c9cc 0%,#fbe3e3 45%,rgba(253,247,247,0) 75%)}
.util-links{position:absolute;top:10px;right:104px;font-size:10.5px;color:#222;font-weight:700}
.util-links a{color:#222;text-decoration:none}
.util-links span{margin:0 6px;font-weight:400}
.page{position:absolute;left:96px;top:35px;width:768px;height:1001px;background:var(--white);box-shadow:0 0 4px rgba(0,0,0,.2)}
.header{position:absolute;left:8px;top:8px;width:752px;height:135px;background:var(--magenta)}
.brand{position:absolute;left:10px;top:50px;display:flex;align-items:center;gap:8px;color:var(--white);font-size:24px;font-weight:700}
.brand-mark{width:14px;height:14px;background:var(--white)}
.brand small{display:block;font-size:9px;font-weight:700;letter-spacing:1px}
.promo{position:absolute;top:26px;display:flex;gap:6px;align-items:center;color:var(--white);font-size:12px;line-height:1.15}
.promo b{display:block;font-weight:700}
.promo em{font-style:normal;color:var(--yellow);font-size:10px}
.promo-shipping{left:424px}
.promo-cart{left:588px}
.search{position:absolute;left:466px;top:92px;width:276px;height:28px;background:var(--white);border-radius:3px}
.search span{position:absolute;left:8px;top:8px;font-size:10px;font-style:italic;color:#999}
.search-btn{position:absolute;right:4px;top:4px;height:20px;width:68px;background:var(--coral);border-radius:2px;color:var(--white);font-size:10px;font-weight:700;display:flex;align-items:center;justify-content:center;gap:4px}
.nav{position:absolute;left:8px;top:143px;width:752px;height:42px;background:linear-gradient(#6aa862,var(--green-dark));display:flex;justify-content:space-between;align-items:center;padding:0 10px 0 16px}
.nav a{color:var(--white);font-size:12px;font-weight:700;text-decoration:none}
.hero{position:absolute;left:9px;top:188px;width:750px;height:307px;border:2px solid #eee;background:linear-gradient(135deg,var(--peach-light),var(--peach))}
.hero-frame{position:absolute;left:14px;top:18px;width:384px;height:270px;background:var(--white);box-shadow:0 2px 5px rgba(0,0,0,.35);transform:rotate(-.6deg)}
.hero-photo{position:absolute;left:8px;top:8px;right:8px;bottom:8px;background:radial-gradient(ellipse at 50% 50%,#dfe8d8 0%,#6c8a5c 35%,#a88470 65%,#6e5444 100%)}
.hero-copy{position:absolute;left:422px;top:76px;width:312px;font-family:"Courgette",cursive;font-size:27px;line-height:37px;color:var(--white);text-shadow:1px 1px 2px rgba(120,60,30,.4)}
.btn-shop{position:absolute;left:427px;top:209px;width:108px;height:30px;background:var(--magenta);color:var(--white);font-size:15px;font-weight:700;border-radius:2px;display:flex;align-items:center;justify-content:center;letter-spacing:.5px}
.dots{position:absolute;left:432px;top:280px;display:flex;gap:5px}
.dots i{width:11px;height:11px;border-radius:50%;background:#8a9f66}
.dots i:first-child{background:var(--green-dark)}
.section-title{position:absolute;left:9px;top:513px;color:var(--magenta-text);font-size:14px;font-weight:700}
.arrows{position:absolute;right:8px;top:510px}
.cards{position:absolute;left:8px;top:539px;display:flex;gap:16px}
.card{position:relative;width:176px;height:242px;border:1px solid #ddd;text-align:center}
.card::after{content:"";position:absolute;left:10px;right:10px;bottom:-8px;height:6px;background:radial-gradient(ellipse at center,rgba(0,0,0,.18),rgba(0,0,0,0) 70%)}
.card-photo{margin:6px 6px 0;height:111px}
.card h3{margin-top:10px;font-size:14px;font-weight:400;color:#222;letter-spacing:.3px}
.card p{font-size:10px;line-height:1.5;margin:2px 10px 0;color:#444}
.price{font-family:"Marcellus",serif;font-size:19px;color:var(--magenta-text);margin-top:3px}
.card-actions{display:flex;justify-content:space-between;margin:6px 14px 0}
.btn{height:23px;width:64px;font-size:9px;font-weight:700;color:var(--white);display:flex;align-items:center;justify-content:center;border-radius:2px}
.btn-details{background:var(--coral)}
.btn-cart{background:var(--lime);color:#444}
.welcome{position:absolute;left:9px;top:808px;width:488px}
.welcome h2{font-size:17px;font-weight:400;color:var(--green-title)}
.welcome h4{margin-top:7px;font-size:11.5px;font-style:italic;font-weight:700;color:var(--magenta-text)}
.welcome p{font-size:10px;line-height:16px;color:#555;margin-top:1px}
.welcome p+p{margin-top:7px}
.btn-more{position:absolute;left:439px;top:969px;width:65px;height:22px;background:#444;color:var(--white);font-size:9px;font-weight:700;border-radius:3px;display:flex;align-items:center;justify-content:center}
.gifts{position:absolute;left:523px;top:813px;width:237px;height:176px;border:1px solid #ccc}
.gifts-photo{height:124px;background:linear-gradient(160deg,#f4eef0 0%,#8a3a2a 35%,#c8202a 60%,#4c8a3a 100%)}
.gifts-label{height:50px;background:#5f9060;color:var(--white);font-family:"Marcellus",serif;font-size:24px;display:flex;align-items:center;justify-content:center;letter-spacing:.5px}
.footer{position:absolute;left:0;top:1036px;width:960px;height:158px;background:var(--footer-bg)}
.footer h5{font-size:12px;font-weight:700;color:var(--green-title);position:absolute;top:28px}
.footer ul{list-style:none;position:absolute;top:52px;font-size:9.5px;color:#444}
.footer li{height:21.6px}
.connect li{display:flex;gap:8px;align-items:flex-start}
.connect i{width:12px;height:12px;background:#999;display:block;border-radius:2px}
.newsletter-text{position:absolute;left:511px;top:45px;width:190px;font-size:9.5px;line-height:1.45;color:var(--magenta-text)}
.email{position:absolute;left:507px;top:90px;width:152px;height:20px;background:var(--white);border:1px solid #ccc;border-radius:3px;font-size:9.5px;color:#888;padding:3px 8px}
.btn-signup{position:absolute;left:618px;top:117px;width:42px;height:20px;background:var(--coral);color:var(--white);font-size:9px;font-weight:700;border-radius:3px;display:flex;align-items:center;justify-content:center}
.payments{position:absolute;left:727px;top:49px;display:flex;gap:2px}
.payments span{height:20px;padding:0 4px;border:1px solid #333;background:var(--white);font-size:8.5px;font-weight:700;color:#333;display:flex;align-items:center}
.copyright{position:absolute;left:729px;top:96px;font-size:9px;line-height:1.5;color:#555}
.footer-bar{position:absolute;left:0;top:1194px;width:960px;height:6px;background:var(--magenta)}
</style>
</head>
<body>
<div class="blossom blossom-left" role="img" aria-label="Soft pink blossom branches"></div>
<div class="blossom blossom-right" role="img" aria-label="Soft pink blossom branches"></div>

<nav class="util-links"><a href="#">Login</a><span>|</span><a href="#">Register</a><span>|</span><a href="#">Wishlist</a><span>|</span><a href="#">Checkout</a><span>|</span><a href="#">Map of Delivery Area</a></nav>

<div class="page">
  <header class="header">
    <div class="brand"><span class="brand-mark"></span><div>Loren Vasquel<small>FLORAL DESIGNER</small></div></div>
    <div class="promo promo-shipping">
      <svg width="36" height="26" viewBox="0 0 36 26"><rect x="8" y="4" width="20" height="14" fill="#fff"/><path d="M28 8h5l3 5v5h-8z" fill="#fff"/><rect x="0" y="8" width="6" height="2" fill="#fff"/><rect x="2" y="12" width="5" height="2" fill="#fff"/><circle cx="13" cy="21" r="3" fill="#fff"/><circle cx="30" cy="21" r="3" fill="#fff"/></svg>
      <div><b>FREE SHIPPING</b><em>On Sale Over &nbsp;€ 200.00</em></div>
    </div>
    <div class="promo promo-cart">
      <svg width="32" height="28" viewBox="0 0 32 28"><path d="M9 10 L15 2 M23 10 L17 2" stroke="#fff" stroke-width="2" fill="none"/><path d="M2 10h28l-3 16H5z" fill="#fff"/><path d="M10 13v10M16 13v10M22 13v10" stroke="#c8085f" stroke-width="2"/></svg>
      <div><b>MY SHOPPING CART</b><em>Total &nbsp;€ 0.00. (0 Items)</em></div>
    </div>
    <div class="search"><span>Search Entire Shop</span><div class="search-btn">SEARCH <svg width="12" height="12" viewBox="0 0 12 12"><circle cx="5" cy="5" r="3.6" stroke="#fff" stroke-width="1.6" fill="none"/><path d="M7.6 7.6L11 11" stroke="#fff" stroke-width="2"/></svg></div></div>
  </header>

  <nav class="nav"><a href="#">Home</a><a href="#">About Loren Vasquel</a><a href="#">Flower for Delivery</a><a href="#">Gifts &amp; Ideas</a><a href="#">Photo Gallery</a><a href="#">Partners &amp; Links</a><a href="#">Contact Us</a></nav>

  <section class="hero">
    <div class="hero-frame"><div class="hero-photo" role="img" aria-label="White carnation and lily arrangement on a rock"></div></div>
    <div class="hero-copy">Dedicated to Designing<br>&amp; Creating for the<br>Individual...</div>
    <div class="btn-shop">SHOP NOW</div>
    <div class="dots"><i></i><i></i><i></i><i></i></div>
  </section>

  <h2 class="section-title">FEATURED FLOWERS</h2>
  <div class="arrows"><svg width="36" height="16" viewBox="0 0 36 16"><path d="M8 2L2 8l6 6" stroke="#555" stroke-width="2" fill="none"/><path d="M28 2l6 6-6 6" stroke="#555" stroke-width="2" fill="none"/></svg></div>

  <div class="cards">
    <article class="card"><div class="card-photo" role="img" aria-label="Red tulip funeral design" style="background:linear-gradient(150deg,#c82028,#3a7a3a 60%,#d8d8c8)"></div><h3>Wings of Love</h3><p>Red Tulip funeral design. Double ended funeral design.</p><div class="price">€150.00</div><div class="card-actions"><span class="btn btn-details">Details</span><span class="btn btn-cart">Add to Cart</span></div></article>
    <article class="card"><div class="card-photo" role="img" aria-label="Red tulip arrangement on gravel" style="background:radial-gradient(ellipse at 50% 55%,#d0202a 0%,#3f6f3a 50%,#c8c8c4 80%)"></div><h3>Wings of Love</h3><p>Red Tulip funeral design. Double ended funeral design.</p><div class="price">€150.00</div><div class="card-actions"><span class="btn btn-details">Details</span><span class="btn btn-cart">Add to Cart</span></div></article>
    <article class="card"><div class="card-photo" role="img" aria-label="White rose bouquet on dark background" style="background:radial-gradient(ellipse at 50% 45%,#f2ecc8 0%,#c8c4a0 35%,#111 70%)"></div><h3>Wings of Love</h3><p>Red Tulip funeral design. Double ended funeral design.</p><div class="price">€150.00</div><div class="card-actions"><span class="btn btn-details">Details</span><span class="btn btn-cart">Add to Cart</span></div></article>
    <article class="card"><div class="card-photo" role="img" aria-label="Tiered wedding cake with flowers" style="background:linear-gradient(#e8e2d8,#f6f4f0 50%,#5a6a40)"></div><h3>Wings of Love</h3><p>Red Tulip funeral design. Double ended funeral design.</p><div class="price">€150.00</div><div class="card-actions"><span class="btn btn-details">Details</span><span class="btn btn-cart">Add to Cart</span></div></article>
  </div>

  <section class="welcome">
    <h2>Welcome to Our Shop</h2>
    <h4>Welcome to Loren Vasquel Designs, our aim is to inspire!</h4>
    <p>We offer beautiful flowers and plants for all tastes and budgets, and whats more, we will deliver them to your loved ones, a service that is not often found in this area of the Costa Blanca, Spain.</p>
    <p>We offer a wide selection of bouquets, flower arrangements and plants, all of which are gift wrapped. Our flowers are of the finest quality and are supplied direct from Holland. However, should you wish to design your own bouquet, perhaps you love a particular flower, or maybe it has a special meaning, then click on 'design own' in the 'Flowers For Delivery' section, and let your imagination run away with you.</p>
  </section>
  <div class="btn-more">Read More</div>

  <aside class="gifts"><div class="gifts-photo" role="img" aria-label="Gift box with red roses"></div><div class="gifts-label">GIFTS &amp; IDEAS</div></aside>
</div>

<footer class="footer">
  <h5 style="left:102px">Navigation</h5>
  <ul style="left:104px"><li>Home</li><li>About Loren Vasquel</li><li>Flower for Delivery</li><li>Gifts &amp; Ideas</li></ul>
  <ul style="left:224px"><li>The Photo Gallery</li><li>Map of Delivery Area</li><li>Partners &amp; Links</li><li>Contact Us</li></ul>
  <h5 style="left:379px">Connect Us</h5>
  <ul class="connect" style="left:380px"><li><i></i>Friendbook</li><li><i></i>Chirper</li><li><i></i>Circles +</li><li><i></i>Rss Feeds</li></ul>
  <h5 style="left:510px">Newsletter Sign Up</h5>
  <p class="newsletter-text">For Latest Collection and offer on flowers to receive updates from us enter email address</p>
  <div class="email">Enter Email</div>
  <div class="btn-signup">SIGN UP</div>
  <h5 style="left:726px">Payment Method</h5>
  <div class="payments"><span>Purselane</span><span>Corvexa</span><span>Mintracard</span></div>
  <p class="copyright">Copyright © 2013<br>Loren Vasquel Floral Designer</p>
</footer>
<div class="footer-bar"></div>
</body>
</html>
```